I would like to purchase a customized version of a design you have previously submitted - https://www.plomvix.example/design/52904618

We Are a Freight Brokerage company based out of Pennsylvania. Company name is Haulmark Ridge Logistics. Phone number 717-382-9154. Email is haulmarkridgelogistics@quenmail.example please design it with trucks like the front page of this brochure example template or New trucks from USA preferably Torvanes Meridell.

Target Market(s)

Shippers

Industry/Entity Type

Logistics

Requirements
Must have
• must be a brochure not a simple front and back flyer.

Also we would like bulletins to describe what our business offers and what we are geared towards. something that is not to informative that it bores them but something that is eye catching that will attract the person it is meant for to want to take a look at it.
Bulletin Ideas:
WHAT WE DO
“ What sets Haulmark Ridge Logistics apart from other transportation providers? Our mission
is to bring value to customers by gaining an understanding of their business and then delivering customized shipping solutions.
With 30-plus years in asset-based and third-party transportation management, we know how to make it happen.”
*WEKNOWTRANSPORTATION
Looking to control transportation-related costs and find cost-effective alternatives? Haulmark Ridge Logistics provides the transportation know-how to help you create a unique competitive edge - each and every day.
Turn to Haulmark Ridge Logistics and you’ll get:

• Access to freight capacity
• Powerful technology that provides visibility into shipment status and details
• Staff accessibility, including communication routed directly to their mobile devices during non-business hours
• Best-in-breed technology platforms for optimum efficiencies and reporting in brokerage, fleet and transportation management, freight bill audit and payment.
TECHNOLOGY AND VISIBILITY
Power your supply chain by Haulmark Ridge Logistics TMS Technology Solutions, giving you access to best-in-breed systems, capabilities, and reporting to manage your entire transportation processes.
• Supply chain visibility from order entry and dispatch through logistics management and settlement
• Accurate, comprehensive visibility to shipping costs and activities
• Shipment routing, tracking, rating, pricing, and delivery measurement
Performance
SUPPLY CHAIN SOLUTIONS
Our culture at Haulmark Ridge Logistics encourages delivery of high performance in service as well as your shipments.
• Each team member has solid transportation expertise
• Close relationships with our carrier partners and drivers delivering your freight
• Resourceful, accountable, accessible
• Able to make immediate decisions, solve complex problems
• Backed by 10 years in business
OUR FEATURES INCLUDE:
Time saving order management features
Load auto-posting to over 43 leading load boards
Real time FMCSA carrier safety / authority data
Automated carrier due diligence
Smart search truck matching
E-update program emails Shippers with status changes
Flexible invoicing options
Detailed reporting and analytics
Online tracking / order visibility
Key performance metrics dashboard for carrier performance

Address: 452 Ostrow Rd, Calderby Pa 17309

```html
<!DOCTYPE html>
<html lang="en">
<head>
<meta charset="utf-8">
<title>Haulmark Ridge Logistics – Trifold Brochure</title>
<link rel="stylesheet" href="https://fonts.googleapis.com/css2?family=Montserrat:wght@400;600;700;800&family=Open+Sans:wght@400;600&family=Roboto+Slab:wght@800&display=swap">
<style>
  :root{
    --stage:#72767a;
    --charcoal:#2f3033;
    --slate:#8b8d90;
    --red:#d3232a;
    --red-dark:#a5161b;
    --white:#ffffff;
    --ink:#2a2a2c;
    --muted:#c9cacc;
    --frame:#e6e7e9;
  }
  *{box-sizing:border-box;margin:0;padding:0}
  html,body{width:1200px;height:3654px;overflow:hidden}
  body{background:var(--stage);font-family:"Open Sans",Arial,sans-serif;position:relative}

  .spread{position:absolute;left:60px;width:1080px;height:760px;display:flex;box-shadow:0 18px 40px rgba(0,0,0,.35)}
  .spread--outside{top:1027px}
  .spread--inside{top:1867px}
  .panel{position:relative;width:360px;height:760px;overflow:hidden}

  .layer{position:absolute;left:0;top:0;width:100%;height:100%}
  .photo{position:absolute;left:0;width:100%}
  .stripe{position:absolute;left:0;width:100%;height:100%;background:var(--red)}

  .heading{font-family:"Montserrat",Arial,sans-serif;font-weight:800;text-transform:uppercase;letter-spacing:.3px}
  .heading .light{font-weight:400}
  .marker{position:absolute;left:0;width:22px;height:10px;background:var(--red)}

  .brand{font-family:"Montserrat",Arial,sans-serif;font-weight:700;text-transform:uppercase;letter-spacing:1px;text-align:center;display:flex;align-items:center;justify-content:center;gap:8px}
  .brand .dot{width:12px;height:12px;border-radius:50%;background:var(--red);flex:none}

  .copy{font-size:11.5px;line-height:1.45}
  .bullets{list-style:none}
  .bullets li{position:relative;padding-left:18px;margin-bottom:9px;font-size:11.5px;line-height:1.4}
  .bullets li::before{content:"";position:absolute;left:2px;top:5px;width:6px;height:6px;background:var(--red);transform:rotate(45deg)}
  .bullets--dark li::before{background:var(--charcoal)}
  .footer-bar{position:absolute;bottom:14px;height:12px;width:186px;background:var(--red)}

  /* Outside: features panel */
  .features{background:var(--slate);color:var(--white)}
  .features .heading{position:absolute;left:34px;top:40px;font-size:19px}
  .features .marker{top:45px}
  .features .bullets{position:absolute;left:34px;top:84px;width:300px}
  .features .bullets li{font-size:11px;margin-bottom:7px}
  .features .ship{top:0;height:100%;background:linear-gradient(160deg,#1f4a52 0%,#12343b 55%,#0c2227 100%);clip-path:polygon(0 58%,100% 50%,100% 100%,0 100%)}
  .features .band{background:var(--charcoal);clip-path:polygon(0 53%,100% 46%,100% 50%,0 58%)}
  .features .stripe{clip-path:polygon(0 54.5%,55% 50.4%,55% 51.2%,0 55.6%)}

  /* Outside: contact panel */
  .contact{background:var(--charcoal);color:var(--white)}
  .contact .yard{top:0;height:100%;background:linear-gradient(170deg,#d9b6a8 0%,#9a3a34 40%,#5c2a2a 75%,#3a3a3d 100%);clip-path:polygon(0 0,100% 0,100% 40%,0 54%)}
  .contact .stripe{clip-path:polygon(0 52%,40% 46.8%,40% 47.8%,0 53.4%)}
  .contact .brand{position:absolute;top:420px;left:0;width:100%;font-size:14px;color:var(--white)}
  .contact-band{position:absolute;top:494px;left:30px;width:300px;height:26px;background:linear-gradient(90deg,rgba(211,35,42,0) 0%,var(--red) 25%,var(--red) 75%,rgba(211,35,42,0) 100%);font-family:"Montserrat",Arial,sans-serif;font-weight:700;font-size:12px;text-align:center;line-height:26px;text-transform:uppercase}
  .contact-list{position:absolute;top:536px;left:0;width:100%;text-align:center;list-style:none}
  .contact-list li{display:flex;flex-direction:column;align-items:center;margin-bottom:8px;font-size:11.5px;color:var(--muted)}
  .contact-list li.phone{font-family:"Montserrat",Arial,sans-serif;font-weight:600;font-size:16px;color:var(--white)}
  .icon{width:18px;height:18px;border-radius:50%;background:var(--red);margin-bottom:5px;display:flex;align-items:center;justify-content:center}
  .icon svg{width:10px;height:10px}

  /* Outside: cover panel */
  .cover{background:var(--frame);padding:14px}
  .cover-inner{position:relative;width:100%;height:100%;background:var(--white)}
  .cover .brand{position:absolute;top:62px;left:0;width:100%;font-size:16px;color:var(--ink)}
  .cover .truck{top:160px;height:420px;background:linear-gradient(180deg,#cfd3d8 0%,#a9adb2 45%,#6e6a66 75%,#8c7d73 100%)}
  .cover-title{position:absolute;top:584px;left:0;width:100%;text-align:center;font-family:"Roboto Slab","Arial Black",sans-serif;font-weight:800;font-size:24px;line-height:30px;color:var(--ink)}
  .cover-ribbon{position:absolute;top:624px;left:28px;right:28px;height:24px;background:linear-gradient(90deg,rgba(211,35,42,0) 0%,var(--red) 22%,var(--red) 78%,rgba(211,35,42,0) 100%);color:var(--white);font-family:"Montserrat",Arial,sans-serif;font-weight:700;font-size:11.5px;text-transform:uppercase;text-align:center;line-height:24px}
  .cover-base{position:absolute;top:660px;left:0;width:100%;text-align:center;font-family:"Montserrat",Arial,sans-serif;font-weight:600;font-size:9.5px;text-transform:uppercase;color:var(--ink)}
  .cover-rule{position:absolute;top:680px;left:90px;right:90px;height:1px;background:#b9bbbe}
  .cover-web{position:absolute;top:700px;left:0;width:100%;text-align:center;font-size:9.5px;color:var(--ink)}

  /* Inside: left panel */
  .about{background:var(--charcoal);color:var(--white)}
  .about .paper{background:var(--white);clip-path:polygon(0 0,100% 0,100% 52%,0 58%)}
  .about .stripe{clip-path:polygon(0 56%,45% 53.5%,45% 54.5%,0 57.2%)}
  .about .block{position:absolute;left:34px;width:300px;color:var(--ink)}
  .about .heading{font-size:17px;color:var(--ink)}
  .about .what{top:46px}
  .about .know{top:236px}
  .about .copy{margin-top:10px;text-align:justify}
  .about .copy + .copy{margin-top:8px}
  .about .brand{position:absolute;top:446px;right:24px;font-size:11px;color:var(--white)}
  .about .lead{position:absolute;top:496px;left:34px;font-size:11.5px}
  .about .bullets{position:absolute;top:532px;left:34px;width:300px}
  .about .footer-bar{left:86px}

  /* Inside: technology panel */
  .tech{background:var(--charcoal);color:var(--white)}
  .tech .truck{top:0;height:100%;background:linear-gradient(170deg,#c8cdd2 0%,#2f78c4 40%,#1d5c9f 70%,#8d9093 100%);clip-path:polygon(0 55%,100% 48%,100% 100%,0 100%)}
  .tech .stripe{clip-path:polygon(55% 47.6%,100% 44.4%,100% 45.6%,55% 48.8%)}
  .tech .heading{position:absolute;left:34px;top:46px;font-size:17px;line-height:1.25}
  .tech .copy{position:absolute;left:34px;top:108px;width:295px;color:var(--muted);text-align:justify}
  .tech .bullets{position:absolute;left:34px;top:186px;width:295px;color:var(--muted)}
  .tech .bullets li{margin-bottom:14px}

  /* Inside: supply chain panel */
  .supply{background:var(--charcoal);color:var(--white)}
  .supply .sea{top:0;height:100%;background:linear-gradient(160deg,#37b6c2 0%,#1f8f9c 45%,#166a75 100%);clip-path:polygon(0 0,100% 0,100% 52%,0 56%)}
  .supply .stripe{clip-path:polygon(0 54.6%,60% 52.2%,60% 53.2%,0 55.8%)}
  .supply .heading{position:absolute;left:34px;top:430px;font-size:17px;line-height:1.25}
  .supply .marker{top:436px}
  .supply .copy{position:absolute;left:34px;top:486px;width:295px;color:var(--muted)}
  .supply .bullets{position:absolute;left:34px;top:548px;width:295px;color:var(--muted)}
  .supply .footer-bar{left:86px}
</style>
</head>
<body>

<section class="spread spread--outside" aria-label="Brochure outside">
  <div class="panel features">
    <div class="photo ship" role="img" aria-label="Aerial view of a container ship at sea"></div>
    <div class="layer band"></div>
    <div class="stripe"></div>
    <span class="marker"></span>
    <h2 class="heading">Our Features Include:</h2>
    <ul class="bullets bullets--dark">
      <li>Time saving order management features</li>
      <li>Load auto-posting to over 43 leading load boards</li>
      <li>Real time FMCSA carrier safety / authority data</li>
      <li>Automated carrier due diligence</li>
      <li>Smart search truck matching</li>
      <li>E-update program emails Shippers with status changes</li>
      <li>Flexible invoicing options</li>
      <li>Detailed reporting and analytics</li>
      <li>Online tracking / order visibility</li>
      <li>Key performance metrics dashboard for carrier performance</li>
    </ul>
  </div>

  <div class="panel contact">
    <div class="photo yard" role="img" aria-label="Stacked shipping containers with white trucks in a freight yard"></div>
    <div class="stripe"></div>
    <div class="brand"><span class="dot"></span>Haulmark Ridge Logistics</div>
    <div class="contact-band">Contact Us</div>
    <ul class="contact-list">
      <li class="phone"><span class="icon"><svg viewBox="0 0 10 10"><path d="M2 1l2 0 .6 2-1 .8a5 5 0 0 0 2.6 2.6l.8-1 2 .6v2c0 .6-.4 1-1 1A8 8 0 0 1 1 2c0-.6.4-1 1-1z" fill="#fff"/></svg></span>717-382-9154</li>
      <li><span class="icon"><svg viewBox="0 0 10 10"><path d="M5 .5a3.2 3.2 0 0 0-3.2 3.2C1.8 6.2 5 9.5 5 9.5s3.2-3.3 3.2-5.8A3.2 3.2 0 0 0 5 .5zm0 4.4a1.2 1.2 0 1 1 0-2.4 1.2 1.2 0 0 1 0 2.4z" fill="#fff"/></svg></span>452 Ostrow Rd, Calderby Pa 17309</li>
      <li><span class="icon"><svg viewBox="0 0 10 10"><rect x="1" y="2" width="8" height="6" fill="#fff"/><path d="M1 2l4 3.2L9 2" stroke="#d3232a" stroke-width=".9" fill="none"/></svg></span>haulmarkridgelogistics@quenmail.example</li>
      <li><span class="icon"><svg viewBox="0 0 10 10"><circle cx="5" cy="5" r="3.8" fill="none" stroke="#fff" stroke-width=".9"/><path d="M1.2 5h7.6M5 1.2c-2 2.4-2 5.2 0 7.6M5 1.2c2 2.4 2 5.2 0 7.6" stroke="#fff" stroke-width=".8" fill="none"/></svg></span>www.haulmarkridgelogistics.example</li>
    </ul>
  </div>

  <div class="panel cover">
    <div class="cover-inner">
      <div class="brand"><span class="dot"></span>Haulmark Ridge Logistics</div>
      <div class="photo truck" role="img" aria-label="Silver Torvanes Meridell semi truck driving toward the viewer on an open road"></div>
      <h1 class="cover-title">Fast Shipping Relief</h1>
      <div class="cover-ribbon">A Freight Brokerage Company</div>
      <div class="cover-base">Based out of Pennsylvania</div>
      <div class="cover-rule"></div>
      <div class="cover-web">www.haulmarkridgelogistics.example</div>
    </div>
  </div>
</section>

<section class="spread spread--inside" aria-label="Brochure inside">
  <div class="panel about">
    <div class="layer paper"></div>
    <div class="stripe"></div>
    <div class="block what">
      <span class="marker" style="left:-34px;top:5px"></span>
      <h2 class="heading"><span class="light">What</span> We Do :</h2>
      <p class="copy">“ What sets Haulmark Ridge Logistics apart from other transportation providers? Our mission is to bring value to customers by gaining an understanding of their business and then delivering customized shipping solutions.</p>
      <p class="copy">With 10+ years in asset-based and third-party transportation management, we know how to make it happen.”</p>
    </div>
    <div class="block know">
      <span class="marker" style="left:-34px;top:5px"></span>
      <h2 class="heading"><span class="light">We Know</span><br>Transportation</h2>
      <p class="copy">Looking to control transportation-related costs and find cost-effective alternatives? Haulmark Ridge Logistics provides the transportation know-how to help you create a unique competitive edge - each and every day.</p>
    </div>
    <div class="brand"><span class="dot"></span>Haulmark Ridge Logistics</div>
    <p class="lead">Turn to Haulmark Ridge Logistics and you’ll get:</p>
    <ul class="bullets">
      <li>Access to freight capacity</li>
      <li>Powerful technology that provides visibility into shipment status and details</li>
      <li>Staff accessibility, including communication routed directly to their mobile devices during non-business hours</li>
      <li>Best-in-breed technology platforms for optimum efficiencies and reporting in brokerage, fleet and transportation management, freight bill audit and payment.</li>
    </ul>
    <span class="footer-bar"></span>
  </div>

  <div class="panel tech">
    <h2 class="heading">Technology <span class="light">and</span><br>Visibility</h2>
    <p class="copy">Power your supply chain by Haulmark Ridge Logistics TMS Technology Solutions, giving you access to best-in-breed systems, capabilities, and reporting to manage your entire transportation processes.</p>
    <ul class="bullets">
      <li>Supply chain visibility from order entry and dispatch through logistics management and settlement</li>
      <li>Accurate, comprehensive visibility to shipping costs and activities</li>
      <li>Shipment routing, tracking, rating, pricing, and delivery measurement</li>
    </ul>
    <div class="photo truck" role="img" aria-label="Blue Torvanes Meridell semi truck parked beside a warehouse"></div>
    <div class="stripe"></div>
  </div>

  <div class="panel supply">
    <div class="photo sea" role="img" aria-label="Loaded container ship sailing through turquoise water"></div>
    <div class="stripe"></div>
    <span class="marker"></span>
    <h2 class="heading"><span class="light">Supply Chain</span><br>Solutions</h2>
    <p class="copy">Our culture at Haulmark Ridge Logistics encourages delivery of high performance in service as well as your shipments.</p>
    <ul class="bullets">
      <li>Each team member has solid transportation expertise</li>
      <li>Close relationships with our carrier partners and drivers delivering your freight</li>
      <li>Resourceful, accountable, accessible</li>
      <li>Able to make immediate decisions, solve complex problems</li>
      <li>Backed by 10 years in business</li>
    </ul>
    <span class="footer-bar"></span>
  </div>
</section>

</body>
</html>
```